Vemarok Contracting Folder

Creating a design for the cover of our folders that we pass to our customers

Want to keep the same look as our colors and fonts as attached

```html
<!DOCTYPE html>
<html lang="en">
<head>
<meta charset="utf-8">
<title>Vemarok Contracting Folder</title>
<link rel="stylesheet" href="https://fonts.googleapis.com/css2?family=Playfair+Display:wght@400&family=Open+Sans:wght@400;600&display=swap">
<style>
  :root {
    --navy: #2e3790;
    --yellow: #f9d333;
    --lavender: #b0b3da;
    --paper: #ffffff;
    --paper-shade: #e9e9eb;
    --fold: #b9b9bd;
    --slit: #a9a9ad;
    --backdrop: #2a2a2a;
  }
  html, body {
    margin: 0;
    padding: 0;
    width: 1200px;
    height: 928px;
    overflow: hidden;
    background: var(--backdrop);
  }
  .folder {
    display: block;
    width: 1200px;
    height: 928px;
  }
  .brand-name { font-family: "Playfair Display", serif; font-weight: 400; fill: var(--navy); }
  .band-text { font-family: "Open Sans", sans-serif; font-size: 8.5px; fill: #fff; }
  .band-url { font-family: "Open Sans", sans-serif; font-size: 11px; letter-spacing: 2px; fill: #fff; }
  .card-text { font-family: "Open Sans", sans-serif; font-size: 4.6px; fill: #333; }
  .card-name { font-family: "Open Sans", sans-serif; font-weight: 600; font-size: 6.4px; fill: var(--navy); }
  .card-title { font-family: "Open Sans", sans-serif; font-size: 6.4px; fill: #333; }
</style>
</head>
<body>
<svg class="folder" viewBox="0 0 1200 928" xmlns="http://www.w3.org/2000/svg" role="img" aria-label="Vemarok Contracting presentation folder, opened flat">
  <defs>
    <linearGradient id="paper-left" x1="0" y1="0" x2="1" y2="1">
      <stop offset="0" stop-color="var(--paper)"/>
      <stop offset="1" stop-color="#f0f0f1"/>
    </linearGradient>
    <linearGradient id="paper-right" x1="0" y1="0" x2="1" y2="1">
      <stop offset="0" stop-color="#f7f7f8"/>
      <stop offset="1" stop-color="var(--paper-shade)"/>
    </linearGradient>

    <g id="business-card">
      <g class="card-slits" stroke="var(--slit)" stroke-width="2.5">
        <line x1="-8" y1="-7" x2="14" y2="13"/>
        <line x1="191" y1="-7" x2="169" y2="13"/>
        <line x1="-8" y1="111" x2="14" y2="91"/>
        <line x1="191" y1="111" x2="169" y2="91"/>
      </g>
      <rect class="card-face" x="0" y="0" width="183" height="104" fill="#fff"/>
      <text class="brand-name" x="17" y="30" font-size="20" textLength="71" lengthAdjust="spacingAndGlyphs">VEMAROK</text>
      <text class="brand-name" x="19" y="42" font-size="7" textLength="67" lengthAdjust="spacingAndGlyphs">CONTRACTING</text>
      <circle cx="15" cy="65" r="1.8" fill="var(--navy)"/>
      <text class="card-text" x="19" y="66.5">012-345-6789</text>
      <circle cx="15" cy="73" r="1.8" fill="var(--navy)"/>
      <text class="card-text" x="19" y="74.5">info@vemarokcontracting.com</text>
      <circle cx="15" cy="81" r="1.8" fill="var(--navy)"/>
      <text class="card-text" x="19" y="82.5">www.vemarokcontracting.com</text>
      <circle cx="15" cy="93" r="1.8" fill="var(--navy)"/>
      <text class="card-text" x="19" y="94.5">Street Name, City Name, Zipcode 012345</text>
      <text class="card-name" x="173" y="66" text-anchor="end">Your Name</text>
      <text class="card-title" x="173" y="74" text-anchor="end">Title</text>
    </g>
  </defs>

  <!-- inside left panel -->
  <g class="panel panel-left">
    <rect x="129" y="45" width="471" height="590" fill="url(#paper-left)"/>
    <rect x="129" y="45" width="471" height="17" fill="var(--yellow)"/>
    <line x1="129" y1="629" x2="600" y2="629" stroke="var(--lavender)" stroke-width="2"/>
    <rect x="129" y="633" width="471" height="41" fill="var(--navy)"/>
    <g class="contact-line">
      <circle cx="304" cy="646" r="3.2" fill="none" stroke="#fff" stroke-width="1"/>
      <text class="band-text" x="310" y="649" textLength="144" lengthAdjust="spacingAndGlyphs">Street Name, City Name, Zipcode 012345</text>
      <circle cx="233" cy="659" r="3.2" fill="none" stroke="#fff" stroke-width="1"/>
      <text class="band-text" x="240" y="662" textLength="48" lengthAdjust="spacingAndGlyphs">012-345-6789</text>
      <circle cx="298" cy="659" r="3.2" fill="none" stroke="#fff" stroke-width="1"/>
      <text class="band-text" x="304" y="662" textLength="103" lengthAdjust="spacingAndGlyphs">info@vemarokcontracting.com</text>
      <circle cx="416" cy="659" r="3.2" fill="none" stroke="#fff" stroke-width="1"/>
      <text class="band-text" x="422" y="662" textLength="103" lengthAdjust="spacingAndGlyphs">www.vemarokcontracting.com</text>
    </g>
  </g>

  <!-- inside right panel -->
  <g class="panel panel-right">
    <rect x="600" y="45" width="471" height="590" fill="url(#paper-right)"/>
    <rect x="600" y="45" width="471" height="17" fill="var(--yellow)"/>
    <circle cx="664" cy="124" r="45" fill="#fff"/>
    <text class="brand-name" x="722" y="157" font-size="80" textLength="254" lengthAdjust="spacingAndGlyphs">VEMAROK</text>
    <text class="brand-name" x="727" y="193" font-size="24" textLength="224" lengthAdjust="spacingAndGlyphs">CONTRACTING</text>
    <line x1="600" y1="629" x2="1071" y2="629" stroke="var(--lavender)" stroke-width="2"/>
    <rect x="600" y="633" width="471" height="41" fill="var(--navy)"/>
    <text class="band-url" x="836" y="654" text-anchor="middle">www.vemarokcontracting.com</text>
  </g>

  <line class="spine-fold" x1="600" y1="45" x2="600" y2="674" stroke="var(--fold)" stroke-width="2.5"/>

  <!-- pockets -->
  <path class="pocket pocket-left" fill="var(--yellow)"
        d="M88 686 L129 673 L600 673 L584 862 Q582 883 562 883 L129 883 L88 870 Z"/>
  <path class="pocket pocket-right" fill="var(--lavender)"
        d="M1112 686 L1071 673 L600 673 L616 862 Q618 883 638 883 L1071 883 L1112 870 Z"/>

  <use href="#business-card" x="257" y="734"/>
  <use href="#business-card" x="754" y="734"/>
</svg>
</body>
</html>
```